Help me create an awesome book cover for my first book!!

I'm self-publishing my first book that focuses on Christian lifestyle. I am looking to encourage and motivate Christians to live their best lives. I am open to design ideas and aside from not wanting any overtly Christian symbols, I don't have any definitive must-haves or must-not-haves. Overall I am a fan of clean, modern designs. I like blues and greens, but am open to other colors depending on the style and the choice of the designer. The book is titled "Quiet Harvest: Finding Where and How You Stand in Grace". Author is Danny Whitlock. The book is about addressing issues with mind, body, and soul that can prevent you from moving toward your destiny. It also talks about faith and spiritual health. Thanks to all!

```html
<!DOCTYPE html>
<html lang="en">
<head>
<meta charset="utf-8">
<title>Quiet Harvest – Book Cover</title>
<link rel="stylesheet" href="https://fonts.googleapis.com/css2?family=Cinzel:wght@400;500&family=EB+Garamond:ital,wght@0,400;1,400&family=Open+Sans:wght@400&display=swap">
<style>
  :root {
    --paper: #ffffff;
    --ink-blue: #1e4b6b;
    --ink-dark: #2a2a2a;
    --sky-deep: #1b3f73;
    --sky-light: #5a8cc2;
    --ember: #d9541a;
    --ember-light: #f08a2a;
    --slate: #3e5a78;
    --slate-light: #7894b4;
    --subtitle: #3a3a3a;
  }
  html, body { margin: 0; padding: 0; overflow: hidden; background: var(--paper); }
  .cover {
    position: relative; width: 1200px; height: 829px; overflow: hidden;
    background: var(--paper); font-family: "Open Sans", sans-serif;
  }
  .sky { position: absolute; inset: 0; }
  .art {
    position: absolute; left: 780px; top: 30px; width: 264px; height: 300px;
    border-radius: 46% 46% 50% 50% / 40% 40% 60% 60%;
    background: radial-gradient(circle at 50% 45%, var(--ember-light), var(--ember) 55%, rgba(217,84,26,0) 72%);
  }
  /* back cover */
  .blurb {
    position: absolute; left: 42px; top: 68px; width: 459px;
    color: var(--ink-blue); font-size: 14px; line-height: 19.2px; text-align: justify;
  }
  .blurb p { margin: 0 0 19px; }
  .portrait {
    position: absolute; left: 40px; top: 488px; width: 164px; height: 164px;
    border-radius: 50%; background: linear-gradient(160deg, #d8d8d4, #8a8276);
  }
  .bio {
    position: absolute; left: 226px; top: 496px; width: 275px;
    color: var(--ink-blue); font-size: 13.5px; line-height: 18px; text-align: justify; margin: 0;
  }
  .website { position: absolute; left: 42px; top: 734px; font-size: 14px; color: var(--ink-dark); margin: 0; }
  /* spine */
  .spine-title, .spine-author {
    position: absolute; writing-mode: vertical-rl; white-space: nowrap; margin: 0;
  }
  .spine-title {
    left: 573px; top: 176px; font-family: "Cinzel", serif; font-size: 44px; line-height: 1; letter-spacing: 1px;
  }
  .spine-title .word-a { color: var(--ember); }
  .spine-title .word-b { color: var(--slate); }
  .spine-author {
    left: 586px; top: 608px; font-size: 19px; color: var(--ink-dark); letter-spacing: 0.5px;
  }
  /* front */
  .front { position: absolute; left: 700px; top: 380px; width: 450px; text-align: center; }
  .title-main {
    margin: 0; font-family: "Cinzel", serif; font-weight: 400; font-size: 128px; line-height: 1;
    background: linear-gradient(180deg, var(--ember-light), var(--ember));
    -webkit-background-clip: text; background-clip: text; color: transparent;
  }
  .title-sub {
    margin: 4px 0 0; font-family: "Cinzel", serif; font-weight: 400; font-size: 76px; line-height: 1;
    background: linear-gradient(90deg, var(--slate), var(--slate-light), var(--slate));
    -webkit-background-clip: text; background-clip: text; color: transparent;
  }
  .subtitle {
    margin: 16px 0 0; font-family: "EB Garamond", serif; color: var(--subtitle); font-size: 29px; line-height: 1.15;
  }
  .subtitle em { display: block; font-size: 42px; }
  .author { position: absolute; left: 700px; top: 762px; width: 450px; text-align: center; margin: 0;
    font-size: 30px; color: var(--ink-dark); }
</style>
</head>
<body>
<main class="cover">
  <svg class="sky" width="1200" height="829" viewBox="0 0 1200 829" aria-hidden="true">
    <defs>
      <linearGradient id="skyFill" x1="0" y1="0" x2="0.3" y2="1">
        <stop offset="0" stop-color="var(--sky-deep)"/>
        <stop offset="1" stop-color="var(--sky-light)"/>
      </linearGradient>
    </defs>
    <polygon points="376,0 1200,0 1200,146 920,300" fill="url(#skyFill)"/>
  </svg>
  <div class="art" role="img" aria-label="Cracked clay heart with a fresh green leaf, glowing warmly against a night sky"></div>

  <section class="back">
    <div class="blurb">
      <p>The book Open Door: Speak Up. Be Known. Find Rest. is a powerful book about how to get the love you have always dreamed of by taking a look at the blocks you hold to love's entry into your life. The blocks are usually the stories you learned in childhood that have shaped the person you are today. In this book I share some research, but mostly case studies and personal stories that support my idea that all of your adult relationships are based on the stories you developed about yourself while growing up. Book is more of an engaging narrative weaving together the stories, the ideas, and the research, and less of a step-by-step how-to.</p>
      <p>After finding Christ at 17, his self-esteem struggles seemed to lessen some, but confusion over God's goodness, his will and his love along with the role, if any, of the supernatural, left him feeling stagnant on his walk. In his mid-twenties the Holy Spirit led him on a journey to the revelation of believers identity, authority, and dominion in Christ. Despite the revelation of these truths and several more supernatural events, D</p>
    </div>
    <div class="portrait" role="img" aria-label="Author portrait"></div>
    <p class="bio">Danny Whitlock is a coach to followers of Christ. Danny has a desire to inspire and motivate believers to pursue their fullness in Christ and recognize what their Lord and Savior did for them on Calvary. Danny focuses on teaching the goodness of God, and showing followers their identity in Christ.</p>
    <p class="website">www.dannywhitlock.com</p>
  </section>

  <p class="spine-title"><span class="word-a">QUIET</span> <span class="word-b">HARVEST</span></p>
  <p class="spine-author">DANNY WHITLOCK</p>

  <section class="front">
    <h1 class="title-main">QUIET</h1>
    <p class="title-sub">HARVEST</p>
    <p class="subtitle">Finding Where and How You Stand <em>in Grace</em></p>
  </section>
  <p class="author">DANNY WHITLOCK</p>
</main>
</body>
</html>
```